Website - Tides Of Bloom

We are catalysts of change in people's lives.
We work with individuals and professionals to bring about instant substantial & transforming change in their lives.
We provide one-on-one lifestyle coaching by an experienced practitioner.
Our existing website is www.tidesofbloom.biz & this site contains our the basis for the content of our desired new project, so please examine this carefully.
We require a professional and captivating website that will instantly impress, engage invite our readers to click & invest their lives.
Our services do not come cheap, but are second to none.
Our website must be contemporary whilst reflecting indisputable class & ultra-confidence in the success of our work.
Target Market(s)
Those who seek to want to change in their lives. Those aged primarily between 30 and 50 years of age, male or female.
Industry/Entity Type
Work
Look and feel

```html
<!DOCTYPE html>
<html lang="en">
<head>
<meta charset="utf-8">
<title>Tides Of Bloom</title>
<link rel="stylesheet" href="https://fonts.googleapis.com/css2?family=Pontano+Sans&display=swap">
<style>
  :root {
    --bg-dark: #262626;
    --bg-dark-2: #2e2e2e;
    --white: #ffffff;
    --text: #4a4a4a;
    --text-dark: #333333;
    --logo-grey: #a6a6a6;
    --orange: #ee7d45;
    --blue: #3a8fb1;
    --blue-text: #2e8fb3;
    --green: #6aab46;
    --green-text: #6e9a2a;
    --nav-grey: #c1c1c1;
    --hero-panel: #c4c7b5;
    --divider: #c8c8c8;
  }
  * { box-sizing: border-box; margin: 0; padding: 0; }
  html, body { width: 1200px; height: 767px; overflow: hidden; }
  body {
    position: relative;
    background: radial-gradient(ellipse at 50% 40%, var(--bg-dark-2), var(--bg-dark) 70%);
    font-family: "Pontano Sans", Arial, sans-serif;
    color: var(--text);
  }
  .brand { position: absolute; left: 56px; top: 26px; display: flex; align-items: center; gap: 22px; }
  .brand-mark { width: 82px; height: 82px; border-radius: 50%; background: #8a8a8a; }
  .brand-name { color: var(--logo-grey); font-size: 40px; line-height: 40px; }

  .call-now { position: absolute; right: 52px; top: 24px; color: var(--white); font-size: 18px; }
  .call-now .phone { color: var(--orange); }

  .main-nav { position: absolute; left: 592px; top: 64px; width: 608px; height: 41px; }
  .main-nav svg { position: absolute; inset: 0; }
  .nav-link { position: absolute; top: 11px; font-size: 15px; color: var(--white); text-decoration: none; transform: translateX(-50%); }
  .nav-link.contact { color: var(--text-dark); }
  .search-box {
    position: absolute; left: 411px; top: 9px; width: 122px; height: 22px;
    background: var(--white); border: none; font-family: inherit; font-size: 13px;
    padding: 3px 9px; color: #555;
  }
  .search-icon { position: absolute; left: 538px; top: 12px; }

  .content-card {
    position: absolute; left: 52px; top: 169px; width: 1096px; height: 555px;
    background: var(--white); border-radius: 4px;
  }
  .hero {
    position: absolute; left: 2px; top: 2px; width: 1092px; height: 349px;
    background: var(--hero-panel); overflow: hidden; border-radius: 3px 3px 0 0;
  }
  .hero-photo {
    position: absolute; left: 410px; top: 0; width: 682px; height: 349px;
    background:
      linear-gradient(90deg, var(--hero-panel) 0%, rgba(196,199,181,0) 14%),
      linear-gradient(180deg, #e6e6dc 0%, #d9d9cb 42%, #9c9274 66%, #6f6a4e 100%);
  }
  .hero-title { position: absolute; left: 55px; top: 98px; font-size: 33px; color: var(--text-dark); font-weight: 400; }
  .hero-sub { position: absolute; left: 57px; top: 143px; font-size: 22px; line-height: 27px; color: var(--text-dark); }
  .hero-button {
    position: absolute; left: 58px; top: 213px; width: 172px; height: 39px;
    background: var(--orange); color: var(--white); font-size: 22px; line-height: 39px;
    text-align: center; text-decoration: none;
  }
  .slider-dots { position: absolute; left: 42px; top: 325px; display: flex; gap: 6px; }
  .slider-dots span { width: 13px; height: 13px; border-radius: 50%; background: rgba(255,255,255,0.45); }
  .slider-dots span.active { background: var(--white); }

  .welcome { position: absolute; left: 42px; top: 370px; width: 580px; }
  .welcome h1 { color: var(--orange); font-size: 21px; font-weight: 400; margin-bottom: 8px; }
  .welcome p { font-size: 14px; line-height: 19px; margin-bottom: 4px; }

  .column-divider { position: absolute; left: 653px; top: 367px; height: 177px; border-left: 1px dotted var(--divider); }

  .services { position: absolute; left: 708px; top: 373px; width: 360px; }
  .service { margin-bottom: 11px; }
  .service h2 { font-size: 17px; font-weight: 400; margin-bottom: 8px; }
  .service.business h2 { color: var(--blue-text); }
  .service.individual h2 { color: var(--green-text); }
  .service p { font-size: 12.5px; line-height: 16px; }
  .read-more { font-size: 12.5px; color: var(--text); text-decoration: none; }

  .site-footer { position: absolute; left: 53px; right: 52px; top: 738px; display: flex; justify-content: space-between; color: var(--white); font-size: 13.5px; }
  .site-footer a { color: var(--white); text-decoration: none; }
</style>
</head>
<body>
  <header>
    <div class="brand">
      <div class="brand-mark"></div>
      <div class="brand-name">Tides Of<br>Bloom</div>
    </div>
    <div class="call-now">Call Now: <span class="phone">+61 02 5550 1472</span></div>
    <nav class="main-nav">
      <svg width="608" height="41" viewBox="0 0 608 41">
        <path d="M20 0 H608 V41 H20 A20.5 20.5 0 0 1 20 0 Z" fill="var(--nav-grey)"/>
        <path d="M20 0 H120 L102 41 H20 A20.5 20.5 0 0 1 20 0 Z" fill="var(--blue)"/>
        <path d="M120 0 H222 L204 41 H102 Z" fill="var(--green)"/>
        <path d="M222 0 H320 L302 41 H204 Z" fill="var(--orange)"/>
      </svg>
      <a class="nav-link" href="#" style="left:54px">Home</a>
      <a class="nav-link" href="#" style="left:146px">Business</a>
      <a class="nav-link" href="#" style="left:247px">Individual</a>
      <a class="nav-link contact" href="#" style="left:351px">Contact Us</a>
      <input class="search-box" type="text" placeholder="Search...">
      <svg class="search-icon" width="16" height="16" viewBox="0 0 16 16">
        <circle cx="6" cy="6" r="4" fill="none" stroke="#555" stroke-width="2"/>
        <line x1="9" y1="9" x2="15" y2="14" stroke="#555" stroke-width="2.5"/>
      </svg>
    </nav>
  </header>

  <main class="content-card">
    <section class="hero">
      <div class="hero-photo" role="img" aria-label="Businessman in a suit raising both fists in triumph above rolling hills"></div>
      <h2 class="hero-title">Change Is Yours</h2>
      <p class="hero-sub">Create better results through<br>becoming a greater thinker</p>
      <a class="hero-button" href="#">+ Read More</a>
      <div class="slider-dots"><span class="active"></span><span></span><span></span></div>
    </section>

    <section class="welcome">
      <h1>Welcome to our website:</h1>
      <p>Our clients experience their desired instant &amp; permanent transformation, emerging from our consultations ready to take on their world from a vastly different paradigm.</p>
      <p>At Tides Of Bloom, our Master Practitioner will inspire you, shifting your perspective &amp; facilitating your mind with the freedom to realise your dreams.</p>
      <p>Join Arlen Whitcombe, Maris Delacourt, R.T. Ashbury, Corin Halvard, Dane Morrow, Lena Okafor and hundreds of thousands of others who are achieving the life changing, consistent results you are dreaming of now.</p>
    </section>

    <div class="column-divider"></div>

    <section class="services">
      <article class="service business">
        <h2>Inspiring Business Excellence</h2>
        <p>Tides Of Bloom have worked with CEO’s &amp; business owners throughout Australia, as catalysts to their outstanding success.</p>
        <a class="read-more" href="#">+ Read More</a>
      </article>
      <article class="service individual">
        <h2>Individual Shift To An Outstanding Life</h2>
        <p>Tides Of Bloom works every day with people just like you who wish to change their lives.</p>
        <a class="read-more" href="#">+ Read More</a>
      </article>
    </section>
  </main>

  <footer class="site-footer">
    <span>Copyright © 2013 Tides Of Bloom | All Rights Reserved</span>
    <span><a href="#">Home</a> &nbsp;|&nbsp; <a href="#">Business</a> &nbsp;|&nbsp; <a href="#">Individual</a> &nbsp;|&nbsp; <a href="#">Contact Us</a></span>
  </footer>
</body>
</html>
```